Velmorytrips.com web design project + logo design

Hi,

We are a Russian online tour operator - roamquiltex.com

We are looking to tranmsfer our domain to velmorytrips.com. The website and logo need to be velmoryesque - we are not looking to change our functionality, but we need to make the website much more attracitve to clients, much more wild looking but at the same time remaining a professional travel company.

The main concept of the website should be innovative travel (as velmory was an innovator). Alternatively, you could go down the artist route and go down the draw / design your own tour road.

On our website the customer is able to combine travel services (hotels, flights, Visa services, and soon chauffeur, car rental etc...) put it into their basket (the basket definitely has to look better than it is at the moment) and pay for it in one go by card.

We are also stressin our customer support with web chat, call centre etc... (call centre number at the top of the page)

We aim to provide an easy user experience, but we need to make it have some more style, so I will be waiting for what you guys can come up with.
Let me know if you have any questions - skype is: mrkostelin

Industry/Entity Type

It Company

Logo Text

Requirements
Must have
• It is quite a simple task - to take the existing website roamquiltex.com and velmorysize it to create velmorytrips.com, the functionality of the website will remain the same and there are not many pages in the website. Homepage, Checkout step1, Checkout step 2 (you can view both of these if you select a service) and the generic pages for T&C''s, Privacy policy etc...

IMPORTANT UPDATE

We are also looking at how the search results will look in the designs, (please do a search on our website for hotel / flight)

```html
<!DOCTYPE html>
<html lang="en">
<head>
<meta charset="utf-8">
<title>Velmorytrips.com</title>
<link href="https://fonts.googleapis.com/css2?family=Lato:wght@400;700&family=Montserrat:wght@300;400;600&family=Roboto+Slab:wght@700&display=swap" rel="stylesheet">
<style>
:root{
  --green:#6cbd1c;
  --green-dark:#3f8a10;
  --green-tab:#4fa514;
  --brown:#3b1f1a;
  --text:#333;
  --muted:#8a8a8a;
  --footer:#3a3a3a;
  --footer-text:#a9a9a9;
  --white:#fff;
}
*{box-sizing:border-box;margin:0;padding:0}
html,body{width:842px;height:1200px;overflow:hidden}
body{font-family:"Lato",sans-serif;color:var(--text);background:#f6f6f6;position:relative}
.abs{position:absolute}

.hero{left:0;top:0;width:842px;height:395px;
  background:linear-gradient(180deg,#5c9ad6 0%,#9fc6ea 40%,#cfe6ef 62%,#3fb3c4 70%,#e9ddc6 78%,#efe4d2 100%)}
.hero-photo{left:0;top:60px;width:420px;height:335px;
  background:radial-gradient(ellipse at 45% 40%,#e8d9b8 0%,#d8c59c 40%,rgba(216,197,156,0) 72%)}
.logo-box{left:82px;top:0;width:131px;height:88px;background:var(--white);display:flex;align-items:center;justify-content:center;gap:6px}
.logo-box .mark{width:10px;height:10px;background:var(--green);border-radius:50%}
.logo-box .name{font-family:"Montserrat",sans-serif;font-weight:600;font-size:12px;color:var(--brown)}
.callout{left:620px;top:29px;width:130px;text-align:center;color:var(--white);font-family:"Montserrat",sans-serif;font-weight:600;font-size:9.5px;line-height:11px}
.nav{left:248px;top:69px;display:flex;gap:21px;font-size:9.5px;color:#111;font-family:"Montserrat",sans-serif}

.tabs{left:536px;top:114px;display:flex}
.tab{height:28px;color:var(--white);font-size:12px;display:flex;align-items:center;justify-content:center}
.tab.one{width:70px;background:var(--green)}
.tab.two{width:84px;background:var(--green-tab)}
.booking{left:536px;top:142px;width:216px;height:410px;background:var(--green)}
.booking .title{position:absolute;left:16px;top:16px;width:178px;height:24px;border:1px solid rgba(255,255,255,.8);border-top:none;color:var(--white);font-size:20px;font-family:"Montserrat",sans-serif;font-weight:300;padding-left:8px;line-height:20px}
.booking label{position:absolute;left:16px;font-size:9.5px;color:#2f4d10}
.booking .field{position:absolute;left:14px;width:189px;height:24px;background:var(--white);font-family:"Montserrat",sans-serif;font-size:11px;color:#bbb;padding:5px 10px}
.check{position:absolute;left:16px;font-size:9px;color:var(--white);display:flex;align-items:center;gap:6px;font-weight:700}
.check i{width:8px;height:8px;background:var(--white);display:inline-block;font-style:normal;color:#333;font-size:8px;line-height:8px;text-align:center}
.pax{position:absolute;top:285px;left:14px;display:flex;gap:6px;align-items:center}
.pax .box{width:40px;height:20px;background:var(--white);margin-right:8px}
.divider{position:absolute;left:7px;top:371px;width:202px;height:1px;background:rgba(255,255,255,.8)}
.btn-check{position:absolute;left:9px;top:377px;width:115px;height:30px;background:var(--green-dark);color:var(--white);font-weight:700;font-size:12px;display:flex;align-items:center;justify-content:center}
.btn-basket{position:absolute;left:137px;top:377px;height:30px;color:var(--white);font-weight:700;font-size:12px;display:flex;align-items:center}

.section-title{font-family:"Montserrat",sans-serif;font-size:15.5px;color:var(--brown)}
.tours{left:78px;top:447px;display:flex;gap:9px}
.tour{width:105px;height:105px;position:relative;display:flex;flex-direction:column;justify-content:flex-end;align-items:center;padding-bottom:6px;color:var(--white);font-family:"Roboto Slab",serif;font-size:8px;text-align:center;line-height:11px}
.tour .price{font-family:"Lato",sans-serif;font-size:8.5px}
.tour .price sup{font-size:6px}
.t1{background:linear-gradient(160deg,#1b9cc8,#0e6b96)}
.t2{background:linear-gradient(160deg,#b8b39c,#5f6a48)}
.t3{background:linear-gradient(180deg,#7aa0c8,#c9843c 45%,#7a4a22)}
.t4{background:linear-gradient(140deg,#5fa0a8,#c88f5a 60%,#8a5a3a)}

.service-rail{left:88px;top:598px}
.service{position:absolute;left:195px;width:370px}
.service h3{font-family:"Montserrat",sans-serif;font-weight:400;font-size:15.5px;color:#222;margin-bottom:8px}
.service p{font-size:9.5px;line-height:16px;color:var(--muted)}
.service a,.read{font-size:9px;color:#222;text-decoration:none;letter-spacing:.3px}

.side-item{position:absolute;left:584px;width:175px;font-size:9px;line-height:13px;color:var(--muted);display:flex;gap:8px}
.side-item a{color:var(--green);text-decoration:none}
.avatar{width:32px;height:32px;flex:none;background:linear-gradient(180deg,#d9d9d9,#7b8a9a)}
.date{flex:none;width:28px;text-align:center;color:#222;font-size:13px;line-height:13px;padding-top:4px}
.date sup{font-size:7px}
.date small{display:block;font-size:10px}

.dash{left:84px;top:914px;width:680px;border-top:1px dashed #b5b5b5}
.contact-now{left:88px;top:931px;font-size:9.5px;font-weight:700;color:var(--brown);display:flex;align-items:center;gap:10px}
.plus{width:13px;height:13px;border-radius:50%;background:var(--green);color:var(--white);font-size:12px;line-height:12px;text-align:center}
.social{left:684px;top:929px;display:flex;gap:10px}
.social span{width:16px;height:16px;border-radius:50%;background:#444;display:block}

.footer{left:0;top:964px;width:842px;height:199px;background:var(--footer);color:var(--footer-text);font-size:9px;line-height:13px}
.footer h4{position:absolute;top:33px;color:var(--white);font-size:10px;font-weight:700;letter-spacing:.3px}
.f-brand{position:absolute;left:90px;top:32px;font-family:"Montserrat",sans-serif;font-weight:600;font-size:15px;color:#8a8a8a;display:flex;align-items:center;gap:6px}
.f-brand i{width:12px;height:12px;background:#8a8a8a;display:block}
.f-col{position:absolute;width:130px}
.f-col .row{padding:6px 0 7px;border-bottom:1px dashed #5a5a5a}
.f-col .row:last-child{border:none}
.f-col b{color:var(--white);font-weight:700}
.contact-list td{padding-right:14px;vertical-align:top}
.bottom{left:0;top:1163px;width:842px;height:37px;background:var(--white);font-size:9px;color:#444}
.bottom nav{position:absolute;left:94px;top:13px;display:flex;gap:13px}
.bottom .copy{position:absolute;right:88px;top:13px}
</style>
</head>
<body>

<section class="abs hero" role="img" aria-label="Beach scene with a woman in a straw hat on a sun lounger, holiday lights and palm trees by the sea"></section>
<div class="abs hero-photo" role="img" aria-label="Sun lounger and straw hat in the foreground"></div>

<div class="abs logo-box"><span class="mark"></span><span class="name">velmorytrips.com</span></div>
<div class="abs callout">YOU CALL, WE'RE THERE<br>(866-VMTRIPS)</div>
<nav class="abs nav">
  <span>HOME</span><span>DESTINATIONS</span><span>ACTIVITES</span><span>TRIP STYLES</span><span>RESPONSIBLE TRAVEL</span><span>AGENTS</span><span>CONTACT US</span>
</nav>

<div class="abs tabs"><div class="tab one">сторону</div><div class="tab two">Класс</div></div>
<form class="abs booking">
  <div class="title">Check Availablity</div>
  <label style="top:56px">Откуда</label><div class="field" style="top:70px">Password</div>
  <label style="top:102px">Куда</label><div class="field" style="top:116px">Password</div>
  <label style="top:148px">Туда</label><div class="field" style="top:162px">Password</div>
  <label style="top:193px">Обратно</label><div class="field" style="top:207px">Password</div>
  <div class="check" style="top:237px"><i></i>Обратно</div>
  <div class="check" style="top:250px"><i>✓</i>В одну сторону</div>
  <label style="top:269px">Пассажиры</label>
  <div class="pax">
    <svg width="8" height="18" viewBox="0 0 8 18"><circle cx="4" cy="2.5" r="2.2" fill="#111"/><rect x="1" y="5" width="6" height="13" rx="1" fill="#111"/></svg><span class="box"></span>
    <svg width="6" height="14" viewBox="0 0 6 14"><circle cx="3" cy="2" r="1.8" fill="#111"/><rect x="1" y="4" width="4" height="10" rx="1" fill="#111"/></svg><span class="box"></span>
    <svg width="8" height="10" viewBox="0 0 8 10"><circle cx="4" cy="2" r="1.8" fill="#111"/><rect x="1" y="4" width="6" height="6" rx="2" fill="#111"/></svg><span class="box"></span>
  </div>
  <label style="top:320px">Обратно</label><div class="field" style="top:331px">Password</div>
  <div class="divider"></div>
  <div class="btn-check">Check Availability</div>
  <div class="btn-basket">View Basket</div>
</form>

<h2 class="abs section-title" style="left:82px;top:414px">Advanture Travel Anywhere</h2>
<div class="abs tours">
  <div class="tour t1" role="img" aria-label="Aerial photo of a tropical island and lagoon"><div>Maldives Dhoni Cruise</div><div class="price">$1499<sup>USD</sup></div></div>
  <div class="tour t2" role="img" aria-label="Photo of ancient stone temple ruins in a forest"><div>Ultimate Cambodian<br>Adventure</div><div class="price">$1062<sup>USD</sup></div></div>
  <div class="tour t3" role="img" aria-label="Photo of a sandstone fort at sunset"><div>Essential India</div><div class="price">$1399<sup>USD</sup></div></div>
  <div class="tour t4" role="img" aria-label="Photo of a traveller kayaking on a river"><div>Thailand Hike, Bike &amp;<br>Kayak</div><div class="price">$1699<sup>USD</sup></div></div>
</div>

<svg class="abs service-rail" width="88" height="270" viewBox="0 0 88 270">
  <rect x="36" y="30" width="16" height="210" fill="#6cbd1c"/>
  <g fill="#6cbd1c"><circle cx="44" cy="42" r="43"/><circle cx="44" cy="133" r="43"/><circle cx="44" cy="224" r="43"/></g>
  <g fill="#ffffff"><circle cx="44" cy="42" r="39"/><circle cx="44" cy="133" r="39"/><circle cx="44" cy="224" r="39"/></g>
  <g fill="#3b1f1a"><circle cx="44" cy="42" r="37"/><circle cx="44" cy="133" r="37"/><circle cx="44" cy="224" r="37"/></g>
  <g fill="#fff">
    <rect x="30" y="32" width="28" height="20" rx="2" fill="none" stroke="#fff" stroke-width="3"/>
    <rect x="38" y="38" width="12" height="2.5"/>
    <path d="M22 133 L40 129 L50 118 L55 118 L50 129 L64 127 L68 122 L71 122 L69 131 L71 140 L68 140 L64 135 L50 137 L55 148 L50 148 L40 137 Z" transform="rotate(-8 44 133)"/>
    <rect x="28" y="215" width="4" height="20"/><rect x="28" y="225" width="34" height="6"/><rect x="58" y="222" width="4" height="13"/><rect x="33" y="219" width="8" height="6" rx="2"/><rect x="42" y="220" width="16" height="5"/>
  </g>
</svg>

<div class="service" style="top:610px"><h3>Visa Service</h3><p>Contrairement à une opinion répandue, le Lorem Ipsum n'est pas simplement du texte aléatoire. Il trouve ses racines dans une .</p><a href="#">Read More</a></div>
<div class="service" style="top:702px"><h3>Flight Service</h3><p>On sait depuis longtemps que travailler avec du texte lisible et contenant du sens est source de distractions, et empêche de se..</p><a href="#">Read More</a></div>
<div class="service" style="top:793px"><h3>Hotel Service</h3><p>Plusieurs variations de Lorem Ipsum peuvent être trouvées ici ou là, mais la majeure partie d'entre elles a été altérée par.</p><a href="#">Read More</a></div>

<h2 class="abs section-title" style="left:584px;top:595px">Testimonials</h2>
<div class="side-item" style="top:623px"><span class="avatar" role="img" aria-label="Customer portrait"></span><span>Lorem ipsum dolor sit nsectetuer adipiscing elit, sed diam nummy nibh euismod. <a href="#">Read More</a></span></div>
<div class="side-item" style="top:674px"><span class="avatar" role="img" aria-label="Customer portrait"></span><span>Lorem ipsum dolor sit nsectetuer adipiscing elit, sed diam nummy nibh euismod. <a href="#">Read More</a></span></div>

<h2 class="abs section-title" style="left:583px;top:754px">Recent News</h2>
<div class="side-item" style="top:780px"><span class="date">14<sup>th</sup><small>Jun</small></span><span>Lorem ipsum dolor sit nsectetuer adipiscing elit, sed diam nummy nibh euismod. <a href="#">Read More</a></span></div>
<div class="side-item" style="top:831px"><span class="date">10<sup>th</sup><small>Jun</small></span><span>Lorem ipsum dolor sit nsectetuer adipiscing elit, sed diam nummy nibh euismod. <a href="#">Read More</a></span></div>

<div class="abs dash"></div>
<div class="abs contact-now">CONTACT US NOW <span class="plus">+</span></div>
<div class="abs social"><span></span><span></span>
  <svg width="16" height="16" viewBox="0 0 16 16"><circle cx="8" cy="8" r="8" fill="#444"/><circle cx="7.3" cy="7.3" r="3" fill="none" stroke="#fff" stroke-width="1.4"/><path d="M9.5 9.5 L11.8 11.8" stroke="#fff" stroke-width="1.6"/></svg>
</div>

<footer class="abs footer">
  <div class="f-brand"><i></i>velmorytrips.com</div>
  <div class="f-col" style="left:90px;top:92px;width:140px">Le Lorem Ipsum est simplement faux texte employé page. pssion. Lorem Ipsum<br><br>l'imprimerie depuis les années 1500, quand un peintre .</div>

  <h4 style="left:250px">LATEST NEWS</h4>
  <div class="f-col" style="left:251px;top:52px">
    <div class="row">Le Lorem Ipsum est simplement.</div>
    <div class="row">Le Lorem Ipsum est simplement faux texte employé page.</div>
    <div class="row">Le Lorem Ipsum est simplement faux texte employé page.</div>
  </div>

  <h4 style="left:418px">TESTIMONIALS</h4>
  <div class="f-col" style="left:419px;top:54px;width:152px">
    <div class="row">"Le Lorem Ipsum est simplement faux texte employé page."<br><b>Marlen Oskova</b></div>
    <div class="row">Le Lorem Ipsum est simplement faux texte employé page. pression. Lorem Ipsum<br><b>Marlen Oskova</b></div>
  </div>

  <h4 style="left:586px">CONTACT US</h4>
  <div class="f-col" style="left:587px;top:58px;width:132px">
    <div class="row"><table class="contact-list"><tr><td><b>Email</b></td><td>hello@velmorytrips.com</td></tr><tr><td><b>Tel</b></td><td>+12 345 9876</td></tr><tr><td><b>Fax</b></td><td>+12 345 9876</td></tr></table></div>
    <div class="row" style="padding-top:12px"><b style="font-size:10px">Velmorytrips</b><br>345 Some Street, City,<br>Country<br>Postal Code</div>
  </div>
</footer>

<div class="abs bottom">
  <nav><span>Home</span><span>About Us</span><span>Services</span><span>News Matter</span><span>Resources</span><span>Blog</span></nav>
  <div class="copy">Copyright 2012 Website Name. All Rights Reserved.</div>
</div>

</body>
</html>
```